Recipe Card Design

I have a small kitchen store in Livingston Montana, and I would like to have recipe cards (4x6 postcard) designed with my logo, lines for recipe writing, all in black and white. My website is here: www.brambleforkpantry.com

Store

```html
<!DOCTYPE html>
<html lang="en">
<head>
<meta charset="utf-8">
<title>Bramble Fork Pantry – Recipe Card</title>
<link rel="stylesheet" href="https://fonts.googleapis.com/css2?family=Share+Tech+Mono&display=swap">
<style>
  :root {
    --paper: #ffffff;
    --ink: #111111;
    --label: #5a5a5a;
    --rule: #1a1a1a;
    --dash: #6a6a6a;
  }
  html, body {
    margin: 0;
    padding: 0;
    overflow: hidden;
    background: var(--paper);
  }
  .recipe-card {
    position: relative;
    width: 1200px;
    height: 750px;
    background: var(--paper);
    overflow: hidden;
    font-family: "Share Tech Mono", monospace;
  }
  .brand {
    position: absolute;
    left: 86px;
    top: 60px;
    width: 228px;
    text-align: center;
    color: var(--ink);
  }
  .brand-mark {
    width: 26px;
    height: 26px;
    background: var(--ink);
    margin: 0 auto 14px;
  }
  .brand-name {
    font-size: 34px;
    line-height: 1.1;
    letter-spacing: 3px;
    text-transform: uppercase;
    margin: 0;
  }
  .brand-place {
    margin-top: 16px;
    font-size: 13px;
    letter-spacing: 3px;
    text-transform: uppercase;
  }
  .recipe-fields {
    position: absolute;
    left: 411px;
    top: 112px;
    width: 730px;
    color: var(--label);
    font-size: 18px;
    letter-spacing: 2px;
    text-transform: uppercase;
    line-height: 1;
  }
  .field-row {
    display: flex;
    align-items: flex-end;
    height: 36px;
    gap: 6px;
  }
  .field-label {
    white-space: nowrap;
    padding-bottom: 2px;
  }
  .fill-line {
    flex: 1;
    border-bottom: 1.5px solid var(--rule);
    margin-bottom: 3px;
  }
  .fill-line.short {
    flex: 0 0 113px;
    margin-right: 8px;
  }
  .header-rule {
    margin-top: 30px;
    margin-left: -13px;
    height: 5px;
    background: var(--rule);
  }
  .card-lines {
    position: absolute;
    left: 0;
    top: 0;
  }
</style>
</head>
<body>
<main class="recipe-card">
  <div class="brand">
    <div class="brand-mark"></div>
    <p class="brand-name">Bramble Fork Pantry</p>
    <div class="brand-place">Cedar Hollow, Oregon</div>
  </div>

  <section class="recipe-fields">
    <div class="field-row">
      <span class="field-label">For:</span><span class="fill-line"></span>
    </div>
    <div class="field-row">
      <span class="field-label">From the Kitchen of:</span><span class="fill-line"></span>
    </div>
    <div class="field-row">
      <span class="field-label">Prep Time:</span><span class="fill-line short"></span>
      <span class="field-label">Cook Time:</span><span class="fill-line short"></span>
      <span class="field-label">Serves:</span><span class="fill-line"></span>
    </div>
    <div class="header-rule"></div>
  </section>

  <svg class="card-lines" width="1200" height="750" viewBox="0 0 1200 750" aria-hidden="true">
    <g class="writing-lines" stroke="var(--dash)" stroke-width="2" stroke-dasharray="10 6">
      <line x1="28" y1="329" x2="574" y2="329"/><line x1="626" y1="329" x2="1172" y2="329"/>
      <line x1="28" y1="375" x2="574" y2="375"/><line x1="626" y1="375" x2="1172" y2="375"/>
      <line x1="28" y1="423" x2="574" y2="423"/><line x1="626" y1="423" x2="1172" y2="423"/>
      <line x1="28" y1="469" x2="574" y2="469"/><line x1="626" y1="469" x2="1172" y2="469"/>
      <line x1="28" y1="516" x2="574" y2="516"/><line x1="626" y1="516" x2="1172" y2="516"/>
      <line x1="28" y1="562" x2="574" y2="562"/><line x1="626" y1="562" x2="1172" y2="562"/>
      <line x1="28" y1="609" x2="574" y2="609"/><line x1="626" y1="609" x2="1172" y2="609"/>
    </g>

    <g class="footer-rule" stroke="var(--rule)" stroke-width="5">
      <line x1="28" y1="678" x2="560" y2="678"/>
      <line x1="639" y1="678" x2="1176" y2="678"/>
    </g>

    <g class="utensils-icon" stroke="var(--ink)" fill="var(--ink)" stroke-linecap="round">
      <line x1="588" y1="666" x2="628" y2="707" stroke-width="4"/>
      <line x1="626" y1="654" x2="572" y2="707" stroke-width="4"/>
      <ellipse cx="632" cy="647" rx="8" ry="12" transform="rotate(45 632 647)" stroke="none"/>
      <path d="M578 660 Q583 668 590 668 L586 664 Z" stroke-width="3"/>
      <g stroke-width="2.5" fill="none">
        <line x1="566" y1="648" x2="580" y2="662"/>
        <line x1="570" y1="644" x2="583" y2="658"/>
        <line x1="574" y1="640" x2="587" y2="654"/>
        <line x1="578" y1="637" x2="590" y2="651"/>
      </g>
    </g>
  </svg>
</main>
</body>
</html>
```